Weight loss surgery restaurant card

We need to create a card for patients who have undergone weight loss surgery to take to restaurants so they can request smaller meals. These patients have had surgery on their stomach so that they can only consume half to one cup of food at a time. So normal sized restaurant meals are way too big (and cost a lot). This card they can present to the restaurant to communicate the fact that they have had weight loss surgery and therefore request a smaller meal portion at reduced cost

Target Market(s)

Restaurants serving weight loss surgery patients

Industry/Entity Type

Health Care

Contact Information for Business Card

This will be a plastic card similar to business card size.

Requirements
Must have
• The front of the card should include the following text:
• The individual bearing this card has undergone weight loss surgery.
• This surgery restricts portion sizes to between half and one cup of food at a time.
• Please give consideration to allowing smaller portions of your regular meals to be ordered to reduce wastage and excess costs.
• Example: a half size portion priced at two thirds of usual cost.
• The back of the card will have spaces for the person to write certain information. These are the categories that can be filled in by hand:
• Name:
• Procedure performed:
• Date of procedure (month/year):
• Treating Clinic Name:
• Treating Clinic Signature:
• Somewhere down the bottom should be something along the lines of:
• supplied from bernardwhitlow.com.au
Nice to have
• A nice design with imagery/colours etc ... not just the text on a white background! Bright attractive colours preferred.
• I have uploaded my logo ... a roughly triangular image followed by my name etc. The triangular logo image could be used somewhere on the card and this logo can be interchangeable for other clinics who purchase the card.
• **Please note that I don't want my name to be included as part of the logo on the card ... just use the triangular image on the side of the logo without the following name**
• Also, the colouring of the card does not have to reflect my logo colours as I am anticipating interchanging this logo with other logos if other clinics choose to adopt the card. I am interested to see other, more generic, colour choices as well as my logo colours

```html
<!DOCTYPE html>
<html lang="en">
<head>
<meta charset="utf-8">
<title>Weight Loss Surgery Restaurant Card</title>
<link rel="stylesheet" href="https://fonts.googleapis.com/css2?family=Roboto:wght@400;500;700&display=swap">
<style>
  :root {
    --brand-green: #1d7a5c;
    --field-green: #2a6e58;
    --rule-green: #5d9d88;
    --card-white: #ffffff;
    --page-bg: #e9ece9;
    --mark-green: #3a9b73;
  }
  * { margin: 0; padding: 0; box-sizing: border-box; }
  html, body { width: 1200px; height: 1200px; overflow: hidden; }
  body {
    background: var(--page-bg);
    font-family: "Roboto", Arial, sans-serif;
    position: relative;
  }
  .card {
    position: absolute;
    left: 120px;
    width: 960px;
    height: 537px;
    background: var(--card-white);
    overflow: hidden;
    box-shadow: 0 6px 20px rgba(0,0,0,0.15);
  }
  .card--front { top: 40px; }
  .card--back { top: 623px; }

  .clinic-mark {
    position: absolute;
    left: 56px;
    top: 34px;
    width: 42px;
    height: 42px;
    border-radius: 50%;
    background: var(--mark-green);
  }

  .front__panel {
    position: absolute;
    left: 0; right: 0;
    top: 111px; bottom: 0;
    background: var(--brand-green);
  }
  .front__list {
    list-style: none;
    position: absolute;
    left: 38px;
    top: 60px;
  }
  .front__item {
    position: relative;
    padding-left: 24px;
    color: var(--card-white);
    font-size: 19px;
    line-height: 48px;
    height: 48px;
    white-space: nowrap;
  }
  .front__item::before {
    content: "";
    position: absolute;
    left: 0; top: 18px;
    border-left: 10px solid var(--card-white);
    border-top: 6px solid transparent;
    border-bottom: 6px solid transparent;
  }

  .back__form {
    position: absolute;
    left: 61px;
    right: 77px;
    top: 148px;
  }
  .back__row {
    display: flex;
    align-items: flex-end;
    height: 46px;
    color: var(--field-green);
    font-weight: 700;
    font-size: 19px;
    white-space: nowrap;
  }
  .back__row--spaced { margin-top: 50px; justify-content: space-between; }
  .back__fill {
    flex: 1;
    border-bottom: 1.5px solid var(--rule-green);
    margin-left: 10px;
    margin-bottom: 4px;
  }
  .back__fill--full { margin-left: 0; }
  .back__date-part {
    display: inline-block;
    width: 60px;
    border-bottom: 1.5px solid var(--rule-green);
    margin: 0 2px 4px;
  }
  .back__signature { padding-right: 70px; }

  .back__footer {
    position: absolute;
    left: 0; right: 0; bottom: 0;
    height: 42px;
    background: var(--brand-green);
    color: var(--card-white);
    font-size: 15px;
    padding-left: 61px;
    line-height: 42px;
  }
</style>
</head>
<body>

<section class="card card--front">
  <span class="clinic-mark"></span>
  <div class="front__panel">
    <ul class="front__list">
      <li class="front__item">The individual bearing this card has undergone weight loss surgery.</li>
      <li class="front__item">Around 500,000 of these procedures are performed around the world every year.</li>
      <li class="front__item">This surgery restricts portion sizes to between half and one cup of food at a time.</li>
      <li class="front__item">Please give consideration to allowing smaller portions of your regular meals to be</li>
      <li class="front__item">ordered to reduce wastage and excess costs.</li>
      <li class="front__item">Example: a half size portion priced at two thirds of usual cost.</li>
    </ul>
  </div>
</section>

<section class="card card--back">
  <span class="clinic-mark"></span>

  <div class="back__form">
    <div class="back__row">Name:<span class="back__fill"></span></div>
    <div class="back__row">Procedure performed:<span class="back__fill"></span></div>
    <div class="back__row"><span class="back__fill back__fill--full"></span></div>
    <div class="back__row"><span class="back__fill back__fill--full"></span></div>
    <div class="back__row">Date of procedure (month/year):&nbsp;<span class="back__date-part"></span>/<span class="back__date-part"></span>/<span class="back__fill" style="margin-left:2px;"></span></div>
    <div class="back__row back__row--spaced"><span>Treating Clinic Name:</span><span class="back__signature">Treating Clinic Signature</span></div>
  </div>

  <div class="back__footer">Purchased through www.bernardwhitlow.com.au</div>
</section>

</body>
</html>
```